Amber Reed Catering Menu

Design 1 page (double sided is ok) menu for catering company.

A flat non-folding menu. Letter paper sized.
Updates

I'm having trouble adding attachments via Pixel Forum.  I have contacted Pixel Forum and will hopefully have them up soon.  

Industry/Entity Type

Catering

Font styles to use
Serif

Requirements
Must have
• Amber Reed Catering logo

menu items from attachment

Double sided is ok

```html
<!DOCTYPE html>
<html lang="en">
<head>
<meta charset="utf-8">
<title>Amber Reed Catering Menu</title>
<link rel="stylesheet" href="https://fonts.googleapis.com/css2?family=Gelasio:wght@400;700&family=Cormorant+SC:wght@500;600&display=swap">
<style>
  :root {
    --ink: #111111;
    --accent: #1f3fd8;
    --rule: #3a55c8;
    --paper: #ffffff;
  }
  * { margin: 0; padding: 0; box-sizing: border-box; }
  html, body { width: 927px; height: 1200px; overflow: hidden; background: var(--paper); }
  .menu {
    position: relative; width: 927px; height: 1200px;
    font-family: "Gelasio", Georgia, serif; font-size: 16.5px; line-height: 20.6px; color: var(--ink);
  }
  .section-title {
    position: absolute; font-family: "Cormorant SC", "Times New Roman", serif; font-weight: 600;
    color: var(--accent); font-size: 36px; letter-spacing: 3px; line-height: 36px; text-align: center;
  }
  .rule {
    position: absolute; height: 4px;
    background: repeating-linear-gradient(90deg, var(--rule) 0 1px, transparent 1px 2px);
  }
  .rule.fade-left { -webkit-mask-image: linear-gradient(90deg, transparent, #000 60%); mask-image: linear-gradient(90deg, transparent, #000 60%); }
  .rule.fade-right { -webkit-mask-image: linear-gradient(90deg, #000 40%, transparent); mask-image: linear-gradient(90deg, #000 40%, transparent); }
  .rule.full { background: repeating-linear-gradient(90deg, var(--rule) 0 1px, transparent 1px 2px); opacity: .8; }
  .block { position: absolute; }
  .item-name { color: var(--accent); font-weight: 700; }
  .price { font-weight: 400; color: var(--ink); }
  .note { position: absolute; font-size: 16.5px; text-align: center; }
  .smallcaps { font-family: "Cormorant SC", serif; font-weight: 600; color: var(--accent); letter-spacing: 2.5px; font-size: 18px; }
  .centered { text-align: center; }
</style>
</head>
<body>
<main class="menu">

  <!-- Specialty Sandwich -->
  <div class="rule fade-left" style="left:31px; top:63px; width:245px;"></div>
  <div class="rule fade-right" style="left:655px; top:63px; width:250px;"></div>
  <h2 class="section-title" style="left:276px; top:48px; width:375px;">Specialty Sandwich</h2>
  <p class="note" style="left:300px; top:84px; width:327px;">$6.99 per guest</p>

  <div class="block" style="left:55px; top:122px; width:360px;">
    <p class="item-name">Italian Wrap</p>
    <p>Salami, Pepperoni, Ham and Cheese Lettuce Tomato with Italian Dressing</p>
  </div>
  <div class="block" style="left:55px; top:199px; width:360px;">
    <p class="item-name">Southwest Steak Wrap</p>
    <p>Steak, Roasted Red Peppers, Lettuce Cheese with Southwest Dressing</p>
  </div>
  <div class="block" style="left:55px; top:279px; width:360px;">
    <p class="item-name">The Highlander</p>
    <p>Smoked Turkey, Fjellberg Cheese, Tomatoes, Lettuce Honey Dijon Sourdough Bread</p>
  </div>

  <div class="block" style="left:473px; top:122px; width:400px;">
    <p class="item-name">Grilled Vegetarian</p>
    <p>Grilled Veggies with Lettuce, Tomato Balsamic Vinaigrette Wrapper or Bread</p>
  </div>
  <div class="block" style="left:473px; top:199px; width:400px;">
    <p class="item-name">The Traditional</p>
    <p>Roast Beef, Lettuce, Tomatoes, Horseradish Mayonnaise On a Roll</p>
  </div>
  <div class="block" style="left:473px; top:298px; width:400px;">
    <p class="smallcaps">* Custom Foot Long Subs</p>
    <p><span class="smallcaps">Available by Request</span> $13.99 per foot</p>
  </div>

  <!-- Salads -->
  <div class="rule fade-left" style="left:29px; top:393px; width:148px;"></div>
  <div class="rule fade-right" style="left:336px; top:393px; width:122px;"></div>
  <h2 class="section-title" style="left:177px; top:376px; width:159px;">Salads</h2>

  <div class="block" style="left:55px; top:444px; width:395px;">
    <p><span class="item-name">Greek Salad</span> $8.99 per guest</p>
    <p>Mixed Greens, Green Peppers, Kalamato Olives, Feta Cheese, Tomatoes, Greek Peppers Greek Dressing</p>
  </div>
  <div class="block" style="left:55px; top:543px; width:395px;">
    <p><span class="item-name">Grilled Chicken Salad</span> $9.99 per guest</p>
    <p>Grilled Chicken, Roquefort Cheese, and Walnuts with Mixed Greens Balsamic Dressing</p>
  </div>
  <div class="block" style="left:55px; top:622px; width:395px;">
    <p><span class="item-name">Chicken Caesar Salad</span> $9.99 per guest</p>
    <p>Marinated Chicken, Romaine Lettuce, Croutons Creamy Caesar Dressing</p>
  </div>
  <div class="block" style="left:55px; top:701px; width:395px;">
    <p><span class="item-name">Antipasto Salad</span> $9.99 per guest</p>
    <p>Mixed Greens, Ham, Salami, Provolone Cheese, Peppers and Olives Italian Dressing</p>
  </div>
  <div class="block" style="left:55px; top:780px; width:400px;">
    <p><span class="item-name">Chef Salad</span> $9.99 per guest</p>
    <p>Mixed Greens, Turkey, Ham, Cheese, Egg, Tomatoes, Cucumbers, Carrots Choice of Dressing</p>
  </div>

  <!-- Anytime Platters -->
  <div class="rule fade-left" style="left:472px; top:393px; width:50px;"></div>
  <div class="rule fade-right" style="left:832px; top:393px; width:70px;"></div>
  <h2 class="section-title" style="left:515px; top:376px; width:320px;">Anytime Platters</h2>

  <div class="block centered" style="left:560px; top:445px; width:220px;">
    <p>Small feeds 8-10</p>
    <p>Medium feeds 16-20</p>
    <p>Large feeds 26-30</p>
  </div>
  <div class="block" style="left:487px; top:524px; width:400px;">
    <p class="item-name">Vegetable &amp; Dip Platter</p>
    <p>S-$24.99&nbsp;&nbsp; M-$39.99&nbsp;&nbsp; L-$59.99</p>
  </div>
  <div class="block" style="left:487px; top:583px; width:400px;">
    <p class="item-name">Cheese and Crackers Platter</p>
    <p>S-$34.99&nbsp;&nbsp; M-$49.99&nbsp;&nbsp; L-$69.99</p>
  </div>
  <div class="block" style="left:487px; top:642px; width:400px;">
    <p class="item-name">Fresh Fruit Platter</p>
    <p>S-$24.99&nbsp;&nbsp; M-$39.99&nbsp;&nbsp; L-$59.99</p>
  </div>
  <div class="block" style="left:487px; top:701px; width:400px;">
    <p><span class="item-name">Chicken Wing Platter</span> (call for prices)</p>
  </div>

  <!-- Custom Gourmet Pizzas -->
  <div class="rule fade-left" style="left:472px; top:787px; width:55px;"></div>
  <div class="rule fade-right" style="left:835px; top:787px; width:67px;"></div>
  <h2 class="section-title" style="left:520px; top:770px; width:320px; line-height:31px;">Custom Gourmet<br>Pizzas</h2>
  <p class="note" style="left:580px; top:842px; width:200px;">Starting at $9.99</p>

  <!-- Snacks -->
  <div class="rule fade-left" style="left:29px; top:899px; width:148px;"></div>
  <div class="rule fade-right" style="left:328px; top:899px; width:125px;"></div>
  <h2 class="section-title" style="left:177px; top:882px; width:151px;">Snacks</h2>

  <div class="block" style="left:55px; top:932px; width:395px;">
    <p><span class="item-name">Baked Goods</span> $4.99 per guest</p>
    <p>Assorted Cookies and Brownies</p>
    <p>Bottle Water or Can Soda</p>
  </div>
  <div class="block" style="left:55px; top:1011px; width:395px;">
    <p><span class="item-name">Sweet &amp; Salty</span> $4.99 per guest</p>
    <p>Assorted Candy Bars, Popcorn, Assorted Chips</p>
    <p>Bottle Water or Can Soda</p>
  </div>

  <!-- Beverages -->
  <div class="rule fade-left" style="left:472px; top:914px; width:105px;"></div>
  <div class="rule fade-right" style="left:782px; top:914px; width:120px;"></div>
  <h2 class="section-title" style="left:577px; top:897px; width:205px;">Beverages</h2>

  <div class="block" style="left:487px; top:953px; width:420px; line-height:25.8px;">
    <p><span class="item-name">Coffee</span> By the Gallon $17.99 per gallon</p>
    <p><span class="item-name">Orange Juice</span> by the gallon $13.99 per gallon</p>
    <p style="line-height:20.6px; margin:2px 0 3px;"><span class="item-name">Lemonade, Fruit Punch or Tea</span> by the gallon $11.99 per gallon</p>
    <p><span class="item-name">Assorted Hot Tea</span> $.99 each</p>
    <p><span class="item-name">Bo</span>ttled Water $1.49 each</p>
    <p><span class="item-name">Can Soda</span> $1.49 each</p>
  </div>

  <!-- Footer rule -->
  <div class="rule full" style="left:31px; top:1160px; width:871px;"></div>
</main>
</body>
</html>
```